KEV.PRO- Darren Holcombe Fitness- needs a clever business card using the logo, name, info, contact

I need a business card designed for my Online Personal Training company called KEV.PRO, abbreviation for Darren Holcombe Fitness. My company focuses on coaching in personal health and personal growth to unleash your greatest potential. I would like to see designs that use my color scheme of a redish-orange (C:0,M:84,Y:100,K:0), grey, white, black, and my company font is OSWALD. The final design should communicate some aspects of design, health, motivation, growth, in some way. The logo is very important to the company and can be displayed in any of the colors previously mentioned. Must include the company name, my website: www.kev-pro.example , my email: dan@kev-pro.example

Target Market(s)

Personal health, fitness, general public, those who lack knowledge, awareness, and confidence in personal health

Industry/Entity Type

Personal Trainer

Font styles to use
Other font styles liked:
• OSWALD. (Bold, Regular, Light)

Colors
f37122
ffffff
9d9d9d
000000

Requirements
Must have
• Must include the logo, company name, my website: www.kev-pro.example , my email: dan@kev-pro.example
Nice to have
• Variations of the colors scheme of a redish-orange (C:0,M:84,Y:100,K:0), grey, white, black. Logo, card, or text can be in any of these colors.
• Possible quote like "Take control of your personal health to unleash your greatest potential" or "Unleashing your greatness first begins with fitness of the body and mind"

```html
<!DOCTYPE html>
<html lang="en">
<head>
<meta charset="utf-8">
<title>KEV.PRO Business Card</title>
<link href="https://fonts.googleapis.com/css2?family=Oswald:wght@300;400;600;700&display=swap" rel="stylesheet">
<style>
  :root {
    --orange: #f04e23;
    --black: #000000;
    --white: #ffffff;
    --grey: #9d9d9d;
    --stage: #6e6e6e;
    --ink: #111111;
  }
  html, body {
    margin: 0;
    padding: 0;
    width: 1200px;
    height: 1200px;
    overflow: hidden;
    background: var(--stage);
    font-family: "Oswald", sans-serif;
  }
  .canvas {
    position: relative;
    width: 1200px;
    height: 1200px;
  }
  .card {
    position: absolute;
    top: 215px;
    width: 440px;
    height: 770px;
    overflow: hidden;
    box-shadow: 0 12px 30px rgba(0,0,0,0.35);
  }
  /* Front: black brand side */
  .card-front {
    left: 120px;
    background: var(--black);
    color: var(--white);
  }
  .brand-circle {
    position: absolute;
    left: 100px;
    top: 190px;
    width: 236px;
    height: 236px;
    border: 3px solid var(--white);
    border-radius: 50%;
    box-sizing: border-box;
  }
  .brand-name {
    position: absolute;
    left: 0;
    right: 0;
    top: 450px;
    margin: 0;
    text-align: center;
    font-size: 78px;
    font-weight: 700;
    line-height: 1;
    letter-spacing: -1px;
  }
  .brand-tagline {
    position: absolute;
    left: 0;
    right: 0;
    top: 540px;
    margin: 0;
    text-align: center;
    font-size: 21px;
    font-weight: 300;
    letter-spacing: 0;
  }
  /* Back: white contact side */
  .card-back {
    left: 640px;
    background: var(--white);
  }
  .portrait {
    position: absolute;
    left: 238px;
    top: 60px;
    width: 168px;
    height: 168px;
    border-radius: 50%;
    border: 4px solid var(--orange);
    box-sizing: border-box;
    background: radial-gradient(circle at 50% 40%, #9a9a9a 0%, #5c5c5c 70%, #3e3e3e 100%);
  }
  .person-name {
    position: absolute;
    left: 40px;
    top: 262px;
    margin: 0;
    color: var(--orange);
    font-size: 46px;
    font-weight: 700;
    line-height: 1;
    letter-spacing: -0.5px;
  }
  .person-role {
    position: absolute;
    left: 42px;
    top: 330px;
    margin: 0;
    color: var(--orange);
    font-size: 18px;
    font-weight: 300;
    letter-spacing: 11px;
  }
  .accent-bar {
    position: absolute;
    left: 88px;
    top: 452px;
    width: 26px;
    bottom: 0;
    background: var(--orange);
  }
  .contact-list {
    position: absolute;
    left: 128px;
    top: 440px;
    margin: 0;
    padding: 0;
    list-style: none;
  }
  .contact-item {
    display: flex;
    align-items: center;
    gap: 12px;
    height: 40px;
    color: var(--ink);
    font-size: 23px;
    font-weight: 600;
    letter-spacing: -0.3px;
  }
  .contact-icon {
    width: 16px;
    height: 16px;
    flex: none;
  }
</style>
</head>
<body>
<main class="canvas">

  <section class="card card-front" aria-label="Card front">
    <div class="brand-circle" aria-hidden="true"></div>
    <h1 class="brand-name">KEV.PRO</h1>
    <p class="brand-tagline">DARREN HOLCOMBE FITNESS</p>
  </section>

  <section class="card card-back" aria-label="Card back">
    <div class="portrait" role="img" aria-label="Portrait photo of the trainer"></div>
    <h2 class="person-name">Darren Holcombe</h2>
    <p class="person-role">Personal Trainer</p>
    <div class="accent-bar" aria-hidden="true"></div>
    <ul class="contact-list">
      <li class="contact-item">
        <svg class="contact-icon" viewBox="0 0 16 16" aria-hidden="true">
          <rect x="1" y="3" width="14" height="10" fill="var(--orange)"/>
          <polyline points="1,3 8,9 15,3" fill="none" stroke="var(--white)" stroke-width="1.4"/>
        </svg>
        <span>dan@kev-pro.example</span>
      </li>
      <li class="contact-item">
        <svg class="contact-icon" viewBox="0 0 16 16" aria-hidden="true">
          <circle cx="8" cy="8" r="7.5" fill="var(--orange)"/>
          <ellipse cx="8" cy="8" rx="3" ry="7" fill="none" stroke="var(--white)" stroke-width="1"/>
          <line x1="1" y1="8" x2="15" y2="8" stroke="var(--white)" stroke-width="1"/>
          <line x1="2.5" y1="4.5" x2="13.5" y2="4.5" stroke="var(--white)" stroke-width="0.8"/>
          <line x1="2.5" y1="11.5" x2="13.5" y2="11.5" stroke="var(--white)" stroke-width="0.8"/>
        </svg>
        <span>www.kev-pro.example</span>
      </li>
    </ul>
  </section>

</main>
</body>
</html>
```